Front and back cover design for skincare marketing materials

Thank you for showing an interest in my project.
Project Details.

I require a front and back cover for our marketing materials.
·       Front Cover size: 105 mm W x 150 mm H.
·       Back Cover size:  105 mm W x 150 mm H.
·       It must include these two colors. You can use a third color if you wish.
1.     #DBA09D
2.     #FFFFFF
 
Front Cover
·      The front cover will have a faded image of the Kakadu Plum branch and fruit. There are two image files, KP_image-1.jpg and kp_image-2.jpeg. You can use both images, just a portion of them, or source alternative royalty-free images of Kakadu Plum that may better fit the design. These two files have been uploaded.
 
The front cover wording.
Top of the front cover.
a.     The title of the image. “Kakadu Plum”
b.     The brand name, “Velvora Skincare”. The file brand_name.ai uploaded.
 
Bottom of the front cover- Designer's choice of font.
The bottom of the front cover contains three lines of text in the following order.  
1.     Australian Native Ingredients
2.     100% Natural · Organic · Wild-harvested
3.     Australian-Made Premium Skincare
 
Back Cover
·      Back Cover wording.The back cover contains the following words "grown by nature" in white (#FFFFFF) of font Italianno (font_file.ttf) with a background color of #DBA09D as seen in the sample box (sample_box.pdf) right-side panel
 
Please provide one file for the front cover and a separate file for the back cover.
All the elements of the files must be editable.
 
Do NOT use the Curve function on the files, as the text must remain editable/changeable.
 
All assets/resources/files, including fonts not supplied by us but used by the designer, must be named and provided with the finished design.

Target Market(s)

Beauty-minded Asian consumers between the ages of 32 and 75 who take a proactive approach to maintaining younger-looking skin. Those who already know the danger of skin damage caused by skincare containing harsh chemicals choose effective natural/organic solutions to meet their skincare needs. Those who wish a more radiant glow and youthful appearance to their skin. Usually, a two-income middle to high-income bracket couples with a mindset for health and beauty.

Industry/Entity Type

beauty

Font styles to use
Other font styles liked:
• I will provide a font file and a brand name file.

Requirements
Must have
• You must use the two colors provided on the product box. The designer may use a third color.
Nice to have
• some gold colour

```html
<!DOCTYPE html>
<html lang="en">
<head>
<meta charset="utf-8">
<title>Velvora Skincare – Kakadu Plum Covers</title>
<link rel="stylesheet" href="https://fonts.googleapis.com/css2?family=Italianno&family=Poppins:wght@400;500&display=swap">
<style>
  :root {
    --rose: #DBA09D;
    --white: #FFFFFF;
    --brand-rose: #d4918d;
    --stage: #e6e6e6;
    --badge-ring: #d7928d;
    --divider: #5a3a38;
  }
  * { box-sizing: border-box; margin: 0; padding: 0; }
  html, body { width: 805px; height: 1200px; overflow: hidden; }
  body { background: var(--stage); position: relative; font-family: "Poppins", sans-serif; }

  .cover {
    position: absolute;
    top: 650px;
    width: 292px;
    height: 418px;
    overflow: hidden;
    box-shadow: 0 6px 10px rgba(0,0,0,0.25);
  }
  .cover--front { left: 85px; }
  .cover--back { left: 439px; background: var(--rose); }

  .front-image {
    position: absolute; inset: 0;
    background:
      radial-gradient(ellipse 60% 35% at 60% 12%, rgba(255,250,246,0.95), rgba(255,250,246,0) 70%),
      radial-gradient(ellipse 40% 30% at 45% 55%, rgba(214,160,140,0.55), rgba(214,160,140,0) 70%),
      radial-gradient(ellipse 50% 25% at 50% 95%, rgba(214,110,95,0.55), rgba(214,110,95,0) 70%),
      radial-gradient(ellipse 30% 20% at 8% 6%, rgba(230,190,140,0.6), rgba(230,190,140,0) 70%),
      linear-gradient(180deg, #f4d8d0 0%, #f1d6cf 25%, #e2b1a6 50%, #d99c92 75%, #d8907f 100%);
  }

  .brand {
    position: absolute; top: 42px; left: 0; right: 0;
    text-align: center;
    font-family: "Italianno", cursive;
    font-size: 54px;
    line-height: 1;
    color: var(--brand-rose);
  }

  .product-title {
    position: absolute; top: 160px; left: 0; right: 0;
    text-align: center;
    font-family: "Italianno", cursive;
    font-weight: 400;
    font-size: 76px;
    line-height: 0.71;
    color: var(--white);
  }
  .product-title span { display: block; }

  .claims {
    position: absolute; left: 0; right: 0; top: 336px; height: 52px;
  }
  .claim { position: absolute; top: 0; width: 51px; height: 51px; }
  .claim--native { left: 24px; }
  .claim--natural { left: 114px; }
  .claim--made { left: 206px; }
  .claim-divider {
    position: absolute; top: 0; height: 49px;
    border-left: 1px dashed var(--divider);
  }
  .claim-divider--one { left: 91px; }
  .claim-divider--two { left: 188px; }
  .claim text { font-family: "Poppins", sans-serif; font-size: 6.2px; fill: var(--white); letter-spacing: 0.2px; }

  .tagline {
    position: absolute;
    left: 50%; top: 50%;
    transform: translate(-50%, -50%) rotate(-90deg);
    font-family: "Italianno", cursive;
    font-size: 76px;
    line-height: 1;
    color: var(--white);
    white-space: nowrap;
  }
</style>
</head>
<body>
  <section class="cover cover--front">
    <div class="front-image" role="img" aria-label="Faded photograph of a Kakadu plum branch with fruit in soft pink and peach tones"></div>
    <div class="brand">Velvora Skincare</div>
    <h1 class="product-title"><span>Kakadu</span><span>Plum</span></h1>

    <div class="claims">
      <svg class="claim claim--native" viewBox="0 0 60 60">
        <defs><path id="arc-native" d="M30,30 m-22,0 a22,22 0 1,1 44,0 a22,22 0 1,1 -44,0"/></defs>
        <circle cx="30" cy="30" r="29" fill="var(--badge-ring)" stroke="var(--white)" stroke-width="1"/>
        <circle cx="30" cy="30" r="16" fill="var(--white)"/>
        <text><textPath href="#arc-native" startOffset="2%">Australian Native · Ingredients</textPath></text>
      </svg>
      <span class="claim-divider claim-divider--one"></span>
      <svg class="claim claim--natural" viewBox="0 0 60 60">
        <defs><path id="arc-natural" d="M30,30 m-22,0 a22,22 0 1,1 44,0 a22,22 0 1,1 -44,0"/></defs>
        <circle cx="30" cy="30" r="29" fill="var(--badge-ring)" stroke="var(--white)" stroke-width="1"/>
        <circle cx="30" cy="30" r="16" fill="var(--white)"/>
        <text><textPath href="#arc-natural" startOffset="0%">100% Natural · Organic · Wild-harvested</textPath></text>
      </svg>
      <span class="claim-divider claim-divider--two"></span>
      <svg class="claim claim--made" viewBox="0 0 60 60">
        <defs><path id="arc-made" d="M30,30 m-22,0 a22,22 0 1,1 44,0 a22,22 0 1,1 -44,0"/></defs>
        <circle cx="30" cy="30" r="29" fill="var(--badge-ring)" stroke="var(--white)" stroke-width="1"/>
        <circle cx="30" cy="30" r="16" fill="var(--white)"/>
        <text><textPath href="#arc-made" startOffset="0%">Australian-Made · Premium Skincare</textPath></text>
      </svg>
    </div>
  </section>

  <section class="cover cover--back">
    <p class="tagline">grown by nature</p>
  </section>
</body>
</html>
```